Plumbing business cards for plumbing company

Need business cards made for my plumbing company

Darren Holcott
253-555-0187
Darren@TrueFlowPipeworksExample.com
www .TrueFlowpipeworksexample.com

https://brightlanehosting.example/wp-content/uploads/2024/03/TrueFlow-Pipes-Rev-04-01.jpg

https://brightlanehosting.example/wp-content/uploads/2024/03/TrueFlow-Pipes-Rev-02-01.jpg

Contact Information for Business Card

Darren Holcott 253-555-0187 Darren@TrueFlowPipeworksExample.com www .TrueFlowpipeworksexample.com

Colors
0054AA
0677BA
7BADD7
CADEEF
E8F1F8

```html
<!DOCTYPE html>
<html lang="en">
<head>
<meta charset="utf-8">
<title>TrueFlow Pipeworks – Business Cards</title>
<link rel="stylesheet" href="https://fonts.googleapis.com/css2?family=Montserrat:wght@300;400;600;700;800&display=swap">
<style>
  :root {
    --page-bg: #ececec;
    --brand-blue: #043b93;
    --white: #ffffff;
    --shadow: rgba(0, 0, 0, 0.28);
  }
  * { margin: 0; padding: 0; box-sizing: border-box; }
  html, body {
    width: 1200px;
    height: 1200px;
    overflow: hidden;
    background: var(--page-bg);
    font-family: "Montserrat", sans-serif;
  }
  .canvas {
    position: relative;
    width: 1200px;
    height: 1200px;
  }
  .card {
    position: absolute;
    left: 260px;
    width: 680px;
    height: 432px;
    overflow: hidden;
    box-shadow: 0 10px 14px -6px var(--shadow);
  }
  .card--front { top: 85px; background: var(--brand-blue); }
  .card--back { top: 600px; background: var(--white); }

  .icon-pattern {
    position: absolute;
    inset: 0;
    background: var(--brand-blue);
  }
  .front-wordmark {
    position: absolute;
    left: 0;
    right: 0;
    top: 128px;
    text-align: center;
    color: var(--white);
    font-weight: 800;
    text-transform: uppercase;
    line-height: 1.02;
  }
  .front-wordmark .line-one { display: block; font-size: 62px; letter-spacing: 1px; }
  .front-wordmark .line-two { display: block; font-size: 62px; letter-spacing: 1px; }

  .back-band {
    position: absolute;
    inset: 0;
    width: 680px;
    height: 432px;
  }
  .back-wordmark {
    position: absolute;
    left: 58px;
    top: 66px;
    color: var(--brand-blue);
    font-weight: 800;
    font-size: 36px;
    text-transform: uppercase;
    letter-spacing: 0.5px;
  }
  .contact-name,
  .contact-phone {
    position: absolute;
    width: 400px;
    left: 255px;
    text-align: center;
    color: var(--white);
    font-weight: 700;
  }
  .contact-name { top: 222px; font-size: 34px; }
  .contact-phone { top: 268px; font-size: 30px; font-weight: 600; }
  .contact-email,
  .contact-web {
    position: absolute;
    right: 54px;
    color: var(--white);
    text-align: right;
    white-space: nowrap;
  }
  .contact-email { top: 320px; font-size: 20px; font-weight: 300; letter-spacing: 0.3px; }
  .contact-web { top: 360px; font-size: 22px; font-weight: 400; }
</style>
</head>
<body>
<main class="canvas">
  <section class="card card--front">
    <div class="icon-pattern" role="img" aria-label="Faint pattern of plumbing tool and fixture icons on blue"></div>
    <h1 class="front-wordmark">
      <span class="line-one">TrueFlow</span>
      <span class="line-two">Pipeworks</span>
    </h1>
  </section>

  <section class="card card--back">
    <svg class="back-band" viewBox="0 0 680 432" role="img" aria-label="Blue diagonal band with faint pattern of plumbing tool and fixture icons">
      <polygon points="0,269 680,85 680,432 0,432" fill="var(--brand-blue)"/>
    </svg>
    <p class="back-wordmark">TrueFlow Pipeworks</p>
    <p class="contact-name">Darren HOLCOTT</p>
    <p class="contact-phone">253-555-0187</p>
    <p class="contact-email">Darren@TrueFlowPipeworksExample.com</p>
    <p class="contact-web">www .TrueFlowpipeworksexample.com</p>
  </section>
</main>
</body>
</html>
```